Financial Markets Algorithmic Trading solution needs One pager Marketing designs

We are creating Marketing sheets that will be handed to potential clients that will give a broad base of our products available. We are an established Sell side firm in the financial Industry and our product focus is a Technology base solution and we want to showcases our Algorithmic trading suite.
Our customer base is Buy-side Traders,hedge funds, managing directors. We want a clean high end technology based look that will encompass the colors that are in our logo.
We intend to work with the designer after initial design to encompass the theme to other pages we have. So we will need a design that can be part of a set but can stand alone.

** i have uploaded a new File that is the correct File to design to. Please follow the flow of the categories and what resides under those headers. This is key for the delivery of the material****

Target Market(s)

Finance- Buy side firms, geared for meetings and info sheets to be left with clients who are CEO's , Head Traders, Managing Directors

Industry/Entity Type

Financial Service

Font styles to use
Other font styles liked:
• Tw Cen MT

Requirements
Must have
• Must include the logo, and encompass the colors that are in the logo.
• We want this to have a Technology company feel to it. We would like it clean and unique, all while not falling into the normal classic business look.
• Also for this page we would like to keep the layout similar to what we have.
• Please keep the style of lettering
Should not have
• Messy look, overpowering color. no cartoon graphics

```html
<!DOCTYPE html>
<html lang="en">
<head>
<meta charset="utf-8">
<title>Algorithmic Trading Strategy Overview</title>
<link href="https://fonts.googleapis.com/css2?family=Jost:wght@400;500;600;700&display=swap" rel="stylesheet">
<style>
:root{
  --bg:#e4e4e4;
  --paper:#ffffff;
  --ink:#111111;
  --orange:#f27a21;
  --orange-light:#f99a3e;
  --orange-dark:#c85a10;
  --blue:#1a64a3;
  --blue-dark:#0c3f73;
  --navy:#0b2f5c;
  --photo-a:#d9dde2;
  --photo-b:#9fb4c9;
}
*{margin:0;padding:0;box-sizing:border-box}
html,body{width:1200px;height:1013px;overflow:hidden;background:var(--bg)}
body{font-family:"Jost",sans-serif;color:var(--ink)}
.sheet{position:absolute;left:250px;top:15px;width:700px;height:983px;background:var(--paper);overflow:hidden;box-shadow:0 4px 18px rgba(0,0,0,.25)}
.hero{position:absolute;left:0;top:0;width:700px;height:430px}
.brand{position:absolute;left:20px;top:360px;display:flex;align-items:center;gap:10px}
.brand-mark{width:40px;height:40px;border-radius:50%;background:var(--orange)}
.brand-name{font-size:20px;font-weight:500;color:var(--blue)}
.title{position:absolute;left:20px;top:438px;font-size:31px;font-weight:700;letter-spacing:.2px;white-space:nowrap}
.intro{position:absolute;left:20px;top:478px;width:662px;font-size:9.6px;line-height:13.7px;text-align:justify}
.panel{position:absolute;left:0;top:593px;width:700px;height:282px;background:radial-gradient(ellipse at 50% 45%,var(--blue) 0%,var(--blue-dark) 85%)}
.column{position:absolute;top:575px;width:190px;text-align:center;color:#fff}
.col-1{left:19px}.col-2{left:255px}.col-3{left:492px}
.tab{position:relative;width:154px;height:61px;margin:0 auto 10px;background:linear-gradient(var(--orange-light),var(--orange));display:flex;align-items:center;justify-content:center;font-size:17px;font-weight:700;line-height:22px;color:#1b1b1b;text-transform:uppercase}
.tab::before,.tab::after{content:"";position:absolute;top:0;border-bottom:10px solid var(--orange-dark)}
.tab::before{left:-8px;border-left:8px solid transparent}
.tab::after{right:-8px;border-right:8px solid transparent}
.strategy{margin-bottom:12px}
.strategy h3{font-size:15px;font-weight:600;color:var(--orange);text-decoration:underline;margin-bottom:3px}
.strategy p{font-size:8.6px;line-height:12.3px;text-align:justify;text-align-last:center}
.note{font-size:8.6px;text-align:left;padding-left:8px}
.footer{position:absolute;left:0;top:896px;width:700px;height:87px;background:linear-gradient(90deg,var(--orange),var(--orange-light) 50%,var(--orange));border-top:3px solid #fff}
.contact-links{position:absolute;left:34px;top:40px;font-size:10px;font-weight:500;line-height:18px}
.contact-links div,.address{display:flex;align-items:center;gap:8px}
.contact-center{position:absolute;left:0;width:700px;top:8px;text-align:center}
.contact-name{font-size:20px;font-weight:600}
.contact-phone{font-size:22px;font-weight:600;display:flex;justify-content:center;align-items:center;gap:6px}
.address{position:absolute;left:520px;top:40px;font-size:10px;font-weight:500;line-height:13px;align-items:flex-start}
</style>
</head>
<body>
<main class="sheet">
  <svg class="hero" viewBox="0 0 700 430" aria-hidden="false">
    <defs>
      <linearGradient id="photoFill" x1="0" y1="0" x2="1" y2="1">
        <stop offset="0" stop-color="var(--photo-a)"/>
        <stop offset="1" stop-color="var(--photo-b)"/>
      </linearGradient>
    </defs>
    <polygon role="img" aria-label="Photo of a printed stock market bar chart on a desk with a coffee cup, pen and reading glasses" points="0,0 700,0 700,398 0,282" fill="url(#photoFill)"/>
    <polygon points="0,282 700,398 700,415 0,290" fill="var(--navy)"/>
    <polygon points="0,290 700,415 700,424 0,322" fill="var(--orange)"/>
  </svg>

  <div class="brand"><span class="brand-mark"></span><span class="brand-name">Bellmore &amp; Partners</span></div>

  <h1 class="title">Algorithmic Trading Strategy Overview</h1>
  <p class="intro">Bellmore &amp; Partners has partnered with an award winning algorithmic trading platform and developed a custom suite of algorithms designed to ensure high quality execution. Our algorithms incorporate our unique Primary-exchange point of sale order types (eRoute* / dRoute*) seamlessly into each strategy. This integration smooth’s workflow, improves execution quality, ensures greater liquidity sourcing, minimizes information leakage and brings a wide variety of Algo and SOR strategies directly into your OMS, EMS, or proprietary trading platform. In addition, we work in a consultative role to develop custom DMA routes, design algorithms according to client needs or specific requirements, and implement unique routing strategies designed to efficiently touch today’s complex market micro-strategy.</p>

  <div class="panel"></div>

  <section class="column col-1">
    <div class="tab">Liquidity<br>Sourcing</div>
    <div class="strategy"><h3>SOR*</h3><p>Optimizes order placement in lit and dark venues to maximize liquidity capture and minimize information leakage. The strategy balances “Urgency to capture the display quote” vs. opportunities to seek out dark liquidity to minimize information leakage and price improvement.</p></div>
    <div class="strategy"><h3>DARK AGG</h3><p>Manages orderplacement in darkvenues to optimize liquidity capture and reduce information leakage. The strategy attempts to first discover liquidity by slicing optimally sized orders at various venues, and then rebalances intelligently to venues where it has detected liquidity.</p></div>
  </section>

  <section class="column col-2">
    <div class="tab">Schedule<br>Driven</div>
    <div class="strategy"><h3>VWAP*</h3><p>Trades using historical volume profile to target VWAP as the benchmark. The strategy can optionally accept StartTime and EndTime as parameters to schedule trading in a given trading period. The strategy utilizes passive and aggressive trading tactics to achieve liquidity.</p></div>
    <div class="strategy"><h3>TWAP*</h3><p>Similar to the VWAP strategy with a different schedule. The schedule is a constant rate of trading between the given StartTime and EndTime.</p></div>
  </section>

  <section class="column col-3">
    <div class="tab">Dynamic &amp;<br>Adaptive</div>
    <div class="strategy"><h3>POV*</h3><p>Tracks volume from the time the order starts trading and trades according to the specified target participation percentage. Continuous optimizations are made as the order trades to target optima price and liquidity goals.</p></div>
    <div class="strategy"><h3>ARRIVAL PRICE*</h3><p>Manages the trade-off between market impact and volatility (price risk) to optimally execute the order.</p></div>
    <p class="note">*Indicates eRoute/ dRoute</p>
  </section>

  <footer class="footer">
    <div class="contact-center">
      <div class="contact-name">Contact: Dana Whitfield</div>
      <div class="contact-phone">
        <svg width="16" height="18" viewBox="0 0 16 18" aria-hidden="true"><path d="M4 1 L7 5 L5 7 Q7 11 10 13 L12 11 L15 14 L12 17 Q3 14 1 4 Z" fill="#fff"/></svg>
        555-014-2870
      </div>
    </div>
    <div class="contact-links">
      <div><svg width="10" height="8" viewBox="0 0 10 8" aria-hidden="true"><rect width="10" height="8" fill="#fff"/><path d="M0 0 L5 4 L10 0" stroke="var(--orange)" fill="none"/></svg>algosales@bellmorepartners.com</div>
      <div><svg width="10" height="10" viewBox="0 0 10 10" aria-hidden="true"><circle cx="5" cy="5" r="4.5" fill="#fff"/><path d="M0.5 5 H9.5 M5 0.5 V9.5" stroke="var(--orange)"/></svg>www.BellmorePartners.com</div>
    </div>
    <div class="address">
      <svg width="9" height="12" viewBox="0 0 9 12" aria-hidden="true"><path d="M4.5 12 L1 6 A4 4 0 1 1 8 6 Z" fill="#fff"/><circle cx="4.5" cy="4.5" r="1.5" fill="var(--orange)"/></svg>
      <span>48 Harbor Street, New York,<br>NY 10010</span>
    </div>
  </footer>
</main>
</body>
</html>
```